Create a landing page for a new product market combination for an international software company

We are a software company being in the BtoB market for over 20 years. Our product is a software tool that allows for very flexible and versatile cost calculations for companies. We sell to all industries in over 40 countries with 500 clients. We have fairly recently seen a succesfull "competitor" (www.veltrani.com) come up in the niche market of IT costing. This competitor has launched an independent platform with regards to managing IT costs (www.QRSguild.org). In this independent platform standards are set, events are organised and books are written. Since our software can handle all type of costing questions we can en already do play a role in IT costing. We have therefore become a sponsor of the QRS guild. Besides that we came accross the opportunity to buy the URL: www.qrssoftware.com Which we did. We are now looking for a design on that landing page that communicates the fact that the visitor has landed with a company that have in depth knowledge on the QRS subject and provide an effective an affordable tooling for QRS. Currently the difference between the professionalism of our own website (www.pricelumen.com) and that of the competitor (www.veltrani.com) and the independent council (www.qrsguild.org). is too big.

Target Market(s)

BtB with large IT spend

Number of Pages Required

1 page

Colors

Designer to choose colors to be used in the design.

Requirements
Must have
• A proffessional look and feel
Should not have
• Definetely not too much information and wording

```html
<!DOCTYPE html>
<html lang="en">
<head>
<meta charset="utf-8">
<title>QRS Software – Technology Business Management</title>
<link href="https://fonts.googleapis.com/css2?family=Open+Sans:wght@400;600;700;800&display=swap" rel="stylesheet">
<style>
:root{
  --orange:#f26522;
  --navy:#0f2236;
  --navy-2:#173250;
  --ink:#222a33;
  --muted:#6b7480;
  --light:#f1f2f4;
  --line:#dfe2e6;
  --white:#ffffff;
  --footer:#3a3f45;
  --footer-dark:#2c3035;
}
*{box-sizing:border-box;margin:0;padding:0}
html,body{width:1200px;height:2696px;overflow:hidden}
body{font-family:"Open Sans",Arial,sans-serif;color:var(--ink);background:var(--white)}
.page{width:1200px;height:2696px;position:relative}

.topbar{height:20px;background:var(--navy);color:#aab4c0;font-size:10px;display:flex;align-items:center;justify-content:space-between;padding:0 40px}
.topbar .flags{display:flex;gap:6px}
.topbar .flags span{width:16px;height:10px;display:block}

.nav{height:68px;display:flex;align-items:center;justify-content:space-between;padding:0 40px;background:var(--white)}
.brand{font-weight:600;font-size:22px;color:var(--navy)}
.menu{display:flex;align-items:center;gap:28px;font-size:14px;font-weight:600;color:var(--navy)}
.btn{display:inline-block;background:var(--orange);color:var(--white);font-weight:700;font-size:12px;letter-spacing:.5px;padding:9px 22px;border-radius:2px;text-transform:uppercase;white-space:nowrap}
.btn.sm{padding:7px 18px;font-size:11px}
.btn.ghost{background:var(--white);color:var(--ink);border:1px solid var(--line);text-transform:none;font-weight:600}

.hero{height:472px;position:relative;background:linear-gradient(100deg,#0c1c2c 0%,#1b3550 55%,#27496a 100%);color:var(--white)}
.hero .photo{position:absolute;inset:0;background:radial-gradient(ellipse at 75% 45%,rgba(90,130,170,.45),rgba(12,28,44,0) 60%)}
.hero .content{position:absolute;left:120px;top:150px}
.hero h1{font-size:50px;font-weight:800;line-height:1.1}
.hero p{font-size:26px;margin:10px 0 40px;color:#dbe3ec}

.section-title{text-align:center;font-size:30px;font-weight:700;color:var(--navy);line-height:40px}

.conversations{height:440px;background:var(--light);padding-top:56px}
.cards{display:flex;justify-content:center;gap:32px;margin-top:40px}
.card{width:220px;height:250px;background:var(--white);border:1px solid var(--line);text-align:center;padding:30px 20px}
.card svg{width:68px;height:68px}
.card h3{font-size:16px;font-weight:700;margin:16px 0 10px;line-height:1.25}
.card p{font-size:11.5px;color:var(--muted);line-height:1.5}

.culture{height:360px;background:linear-gradient(180deg,#d9dce0 0%,#f6f7f8 60%,#e6e8eb 100%);padding-top:48px}
.culture .cols{display:flex;justify-content:center;gap:200px;margin-top:28px}
.culture .col{width:320px;text-align:center;display:flex;flex-direction:column;align-items:center}
.culture svg{width:88px;height:70px}
.culture h3{font-size:17px;font-weight:700;margin:8px 0 10px;line-height:24px}
.culture p{font-size:11.5px;color:var(--muted);line-height:17px;height:51px;text-align:left;margin-bottom:14px}
.culture .col .btn{align-self:flex-end}

.value{height:460px;background:linear-gradient(180deg,var(--navy) 0%,var(--navy-2) 100%);color:var(--white);padding-top:60px;text-align:center}
.value .section-title{color:var(--white)}
.pillars{display:flex;justify-content:center;gap:50px;margin:44px 0 30px}
.pillar{width:210px}
.pillar .icon{width:70px;height:70px;background:var(--orange);border-radius:8px;margin:0 auto;display:flex;align-items:center;justify-content:center}
.pillar .icon svg{width:40px;height:40px}
.pillar h3{font-size:17px;font-weight:700;margin:16px 0 8px;line-height:1.25}
.pillar p{font-size:11.5px;color:#b7c3d0;line-height:1.5}

.news{height:500px;background:var(--light);padding-top:50px}
.news-grid{display:flex;justify-content:center;gap:40px;margin-top:36px}
.news-card{width:460px;background:var(--white);border:1px solid var(--line);padding:16px}
.news-card .photo{height:190px}
.news-card .tag{display:inline-block;background:var(--orange);color:var(--white);font-size:10px;font-weight:700;padding:3px 10px;margin:14px 0 8px}
.news-card h3{font-size:16px;font-weight:700;margin-bottom:8px}
.news-card p{font-size:11px;color:var(--muted);line-height:1.5}

.join{height:160px;background:var(--white);display:flex;align-items:center;justify-content:center;gap:60px}
.join h2{font-size:28px;font-weight:700;color:var(--navy)}
.join p{font-size:12px;color:var(--muted);margin-top:4px}
.join .form{display:flex}
.join .input{width:240px;height:38px;border:1px solid var(--line);background:var(--light)}
.join .btn{height:38px;line-height:20px;border-radius:0}

.footer{height:192px;background:var(--footer);color:#c3c8ce;display:flex;justify-content:center;gap:62px;padding-top:34px}
.footer h4{color:var(--white);font-size:13px;font-weight:700;margin-bottom:10px}
.footer li{list-style:none;font-size:11px;line-height:1.7}
.bottombar{height:24px;background:var(--footer-dark);color:#9aa1a9;font-size:10px;text-align:center;line-height:24px}
</style>
</head>
<body>
<div class="page">

  <div class="topbar">
    <span>Helpdesk +31 (0)20 555 0142 | Fax +31 (0)20 555 0143</span>
    <span class="flags"><span style="background:#c8202f"></span><span style="background:#1f3f8f"></span><span style="background:#e8e8e8"></span></span>
  </div>

  <header class="nav">
    <div class="brand">QRS Software</div>
    <nav class="menu">
      <span>Who We Are</span><span>Learn QRS</span><span>Awards</span><span>Events</span><span>Emerge</span>
      <span class="btn sm">Join Us</span>
    </nav>
  </header>

  <section class="hero">
    <div class="photo" role="img" aria-label="Business team working with technology, dark blue tones"></div>
    <div class="content">
      <h1>Technology Business<br>Management</h1>
      <p>Effective and affordable</p>
      <span class="btn">Show More</span>
    </div>
  </section>

  <section class="conversations">
    <h2 class="section-title">Enable The Right Business Conversations</h2>
    <div class="cards">
      <div class="card">
        <svg viewBox="0 0 68 68"><circle cx="34" cy="34" r="30" fill="var(--orange)"/><text x="34" y="46" text-anchor="middle" font-size="34" font-weight="700" fill="#fff" font-family="Open Sans,sans-serif">$</text></svg>
        <h3>Cost Of<br>Performance</h3>
        <p>Deliver technology, services and projects efficiently to the business.</p>
      </div>
      <div class="card">
        <svg viewBox="0 0 68 68"><rect x="18" y="8" width="32" height="52" fill="var(--orange)"/><g fill="#fff"><rect x="23" y="14" width="6" height="6"/><rect x="31" y="14" width="6" height="6"/><rect x="39" y="14" width="6" height="6"/><rect x="23" y="24" width="6" height="6"/><rect x="31" y="24" width="6" height="6"/><rect x="39" y="24" width="6" height="6"/><rect x="23" y="34" width="6" height="6"/><rect x="31" y="34" width="6" height="6"/><rect x="39" y="34" width="6" height="6"/><rect x="30" y="46" width="8" height="14"/></g></svg>
        <h3>Business-Aligned<br>Portfolio</h3>
        <p>Optimize portfolios to deliver the most value for the level of spending.</p>
      </div>
      <div class="card">
        <svg viewBox="0 0 68 68"><circle cx="34" cy="28" r="18" fill="var(--orange)"/><rect x="27" y="44" width="14" height="10" fill="var(--orange)"/><rect x="29" y="56" width="10" height="4" fill="var(--orange)"/><path d="M34 16 L28 30 H35 L32 40 L41 25 H34 Z" fill="#fff"/></svg>
        <h3>Investment In<br>Innovation</h3>
        <p>Allocate adequate resources on new and enhanced services and on business innovation.</p>
      </div>
      <div class="card">
        <svg viewBox="0 0 68 68"><circle cx="34" cy="34" r="28" fill="var(--orange)"/><g fill="none" stroke="#fff" stroke-width="2.5"><ellipse cx="34" cy="34" rx="12" ry="28"/><line x1="6" y1="34" x2="62" y2="34"/><path d="M11 20 H57 M11 48 H57"/></g></svg>
        <h3>Enterprise<br>Agility</h3>
        <p>Help the business respond quickly to market opportunities or threats.</p>
      </div>
    </div>
  </section>

  <section class="culture">
    <h2 class="section-title">Foster a Business Culture in IT</h2>
    <div class="cols">
      <div class="col">
        <svg viewBox="0 0 88 70"><g fill="var(--navy)"><circle cx="20" cy="22" r="9"/><path d="M6 58 Q6 36 20 36 Q34 36 34 58Z"/><circle cx="68" cy="22" r="9"/><path d="M54 58 Q54 36 68 36 Q82 36 82 58Z"/></g><g fill="var(--orange)"><circle cx="44" cy="16" r="11"/><path d="M26 64 Q26 34 44 34 Q62 34 62 64Z"/></g></svg>
        <h3>Position for Value</h3>
        <p>Define what you deliver in terms of business capabilities that are understood and valued by your business and partners, so you can work together to improve outcomes.</p>
        <span class="btn sm ghost">Read More</span>
      </div>
      <div class="col">
        <svg viewBox="0 0 88 70"><circle cx="34" cy="38" r="20" fill="none" stroke="var(--orange)" stroke-width="10" stroke-dasharray="8 5"/><circle cx="34" cy="38" r="8" fill="var(--orange)"/><circle cx="64" cy="20" r="12" fill="none" stroke="var(--navy)" stroke-width="7" stroke-dasharray="6 4"/><circle cx="64" cy="20" r="4" fill="var(--navy)"/></svg>
        <h3>Continuously Improve</h3>
        <p>Execute a strategic roadmap for QRS maturity by integrating QRS into your day-to-day processes, so QRS drives every value conversation.</p>
        <span class="btn sm ghost">Read More</span>
      </div>
    </div>
  </section>

  <section class="value">
    <h2 class="section-title">Enable The Right Business Conversations</h2>
    <div class="pillars">
      <div class="pillar">
        <div class="icon"><svg viewBox="0 0 40 40"><path d="M2 20 Q20 4 38 20 Q20 36 2 20Z" fill="none" stroke="#fff" stroke-width="3"/><circle cx="20" cy="20" r="6" fill="#fff"/></svg></div>
        <h3>Create<br>Transparency</h3>
        <p>Translate your spending, consumption, and capacity into meaningful perspectives for technology and business decision makers.</p>
      </div>
      <div class="pillar">
        <div class="icon"><svg viewBox="0 0 40 40"><g fill="#fff"><rect x="4" y="26" width="7" height="10"/><rect x="14" y="18" width="7" height="18"/><rect x="24" y="12" width="7" height="24"/></g><path d="M4 18 L16 9 L24 13 L36 4" fill="none" stroke="#fff" stroke-width="3"/></svg></div>
        <h3>Shape<br>Business Demand</h3>
        <p>Communicate costs and consumption to business units to drive informed trade-off decisions and better consumption behavior.</p>
      </div>
      <div class="pillar">
        <div class="icon"><svg viewBox="0 0 40 40"><rect x="4" y="4" width="32" height="32" rx="3" fill="none" stroke="#fff" stroke-width="3"/><text x="20" y="30" text-anchor="middle" font-size="24" font-weight="700" fill="#fff" font-family="Open Sans,sans-serif">$</text></svg></div>
        <h3>Deliver Value<br>For Money</h3>
        <p>Maximize value and demonstrate industry-comparable cost effectiveness for services and innovation you provide.</p>
      </div>
      <div class="pillar">
        <div class="icon"><svg viewBox="0 0 40 40"><rect x="8" y="6" width="24" height="30" rx="2" fill="none" stroke="#fff" stroke-width="3"/><rect x="14" y="3" width="12" height="6" fill="#fff"/><path d="M13 22 L18 27 L28 16" fill="none" stroke="#fff" stroke-width="3"/></svg></div>
        <h3>Plan &amp;<br>Govern</h3>
        <p>Collaborate to align your annual budget and resource plans to strategic business priorities and manage to the plan.</p>
      </div>
    </div>
    <span class="btn sm">Read More</span>
  </section>

  <section class="news">
    <h2 class="section-title">News</h2>
    <div class="news-grid">
      <article class="news-card">
        <div class="photo" role="img" aria-label="Speaker presenting at a business event" style="background:linear-gradient(135deg,#5d6a78,#b9a58c)"></div>
        <span class="tag">Event</span>
        <h3>PriceLumen QRS Cost model</h3>
        <p>Define what you deliver in terms of business capabilities that are understood and valued by your business and partners, so you can work together to improve outcomes.</p>
      </article>
      <article class="news-card">
        <div class="photo" role="img" aria-label="Group of training course participants" style="background:linear-gradient(135deg,#c9b79d,#7d8a97)"></div>
        <span class="tag">Event</span>
        <h3>Cost Management Training Course Vietnam</h3>
        <p>Define what you deliver in terms of business capabilities that are understood and valued by your business and partners, so you can work together to improve outcomes.</p>
      </article>
    </div>
  </section>

  <section class="join">
    <div>
      <h2>Join the most happening community</h2>
      <p>Stay informed on QRS news, events and practical costing insights.</p>
    </div>
    <div class="form"><div class="input"></div><span class="btn">Subscribe</span></div>
  </section>

  <footer class="footer">
    <div><h4>Product</h4><ul><li>Features</li><li>Modules</li><li>Pricing</li><li>Downloads</li></ul></div>
    <div><h4>Markets</h4><ul><li>IT Costing</li><li>Finance</li><li>Healthcare</li><li>Logistics</li></ul></div>
    <div><h4>Partner</h4><ul><li>Become a Partner</li><li>Partner Network</li><li>QRS Guild</li></ul></div>
    <div><h4>Support</h4><ul><li>Helpdesk</li><li>Training</li><li>Documentation</li><li>FAQ</li></ul></div>
    <div><h4>Contact Netherlands</h4><ul><li>Keizersgracht 100</li><li>1015 AA Amsterdam</li><li>+31 (0)20 555 0142</li><li>info@qrssoftware.com</li></ul></div>
    <div><h4>Contact USA</h4><ul><li>200 Harbor Street</li><li>Boston, MA 02110</li><li>+1 617 555 0188</li><li>usa@qrssoftware.com</li></ul></div>
  </footer>
  <div class="bottombar">© 2017 QRS Software. All rights reserved | Terms of use</div>

</div>
</body>
</html>
```